Multifamily Investment Strategies

I need a pamphlet or booklet for multifamily commercial real estate investment.

The specific investment vehicle is affordable multifamily apartments. I have uploaded a 5 page pdf detailing my investment strategy.

The target audience for this pamphlet are investors, commercial brokers, and commercial bankers.

I am looking for modern, clean design that is striking and professional but also eye catching.
Updates

I made a few changes to the brief and also corrected two errors.

Target Market(s)

Commercial Real Estate Investors, Brokers, and Bankers

Industry/Entity Type

Real Estate

Font styles to use
Serif

Colors

Designer to choose colors to be used in the design.

Requirements
Must have
• Graphics of or related to apartment buildings.
• My headshot seen on the last page of the pdf
Nice to have
• Imagery related to investment and profits.
Should not have
• The image of an apartment building on the first page of the pdf is just an example. Please don’t use this image.

```html
<!DOCTYPE html>
<html lang="en">
<head>
<meta charset="utf-8">
<title>Multifamily Cashflow Investment Strategy – Brochure</title>
<link rel="stylesheet" href="https://fonts.googleapis.com/css2?family=Open+Sans:wght@300;400;600;700&display=swap">
<style>
:root{
  --page-bg:#e9eaec;
  --paper:#ffffff;
  --blue:#1a8fd6;
  --blue-deep:#0b5c9e;
  --cyan:#22a6e3;
  --title-blue:#1777c4;
  --charcoal:#333438;
  --ink:#3c3c3c;
  --muted:#5b5b5b;
  --panel-grey:#e6e8eb;
}
*{box-sizing:border-box;margin:0;padding:0}
html,body{width:900px;height:1200px;overflow:hidden}
body{background:var(--page-bg);font-family:"Open Sans",Arial,sans-serif;color:var(--ink);position:relative}
.spread{position:absolute;left:45px;width:810px;height:524px;background:var(--paper);box-shadow:0 14px 18px -8px rgba(0,0,0,.35)}
.spread--outer{top:40px}
.spread--inner{top:618px}
.page{position:absolute;top:0;width:405px;height:100%;overflow:hidden}
.page--left{left:0}
.page--right{left:405px}
.page--left::after{content:"";position:absolute;right:0;top:0;width:40px;height:100%;background:linear-gradient(90deg,rgba(0,0,0,0),rgba(0,0,0,.08))}
.page--right::before{content:"";position:absolute;left:0;top:0;width:30px;height:100%;background:linear-gradient(90deg,rgba(0,0,0,.07),rgba(0,0,0,0));z-index:3;pointer-events:none}
.abs{position:absolute}
.photo{position:absolute}
.footer-bar{position:absolute;left:0;bottom:0;width:100%;height:14px;background:var(--charcoal)}

/* outer spread – back cover */
.townhouse-photo{left:0;top:0;width:405px;height:210px;background:linear-gradient(180deg,#9fc3e4 0%,#c9d9e6 35%,#a35b43 55%,#8c6c55 75%,#5f8a3e 100%)}
.profile-panel{left:0;top:210px;width:405px;height:172px;background:linear-gradient(90deg,var(--cyan) 0%,#1578bf 60%,var(--blue-deep) 100%)}
.headshot{left:157px;top:174px;width:92px;height:92px;border-radius:50%;border:4px solid #dfe3e7;background:radial-gradient(circle at 50% 40%,#9a9a9a,#4a4a4a);z-index:2}
.profile-name{left:0;top:280px;width:405px;text-align:center;color:#fff;font-weight:300;font-size:12px}
.profile-bio{left:15px;top:304px;width:380px;color:#fff;font-size:7.6px;line-height:1.38;text-align:justify}
.plan-sketch{left:0;top:382px;width:150px;height:128px;background:linear-gradient(135deg,#f1f2f4 0%,#ffffff 80%)}
.contact-list{left:224px;top:426px;list-style:none}
.contact-list li{display:flex;align-items:center;height:18px;font-size:10px;color:#444}
.contact-list .ico{width:11px;height:11px;margin-right:9px;background:#9aa0a6;border-radius:2px;display:flex;align-items:center;justify-content:center}

/* outer spread – front cover */
.cover-title{left:0;top:42px;width:405px;text-align:center;color:var(--title-blue);font-size:13.4px;font-weight:400;letter-spacing:.1px}
.cover-band{left:0;top:88px;width:405px;height:42px;background:var(--cyan)}
.house-photo{left:0;top:130px;width:405px;height:252px;background:linear-gradient(180deg,#2f5aa8 0%,#8fb0d8 35%,#c49a78 55%,#8d7462 72%,#4d8a35 88%,#3e7228 100%)}
.cover-accent{left:185px;top:382px;width:220px;height:6px;background:var(--blue)}
.cover-tagline{left:0;top:410px;width:405px;text-align:center;color:#555;font-size:15.5px;font-weight:300;line-height:1.52}

/* inner spread – left */
.couple-photo{left:74px;top:21px;width:331px;height:204px;background:linear-gradient(180deg,#dfe6ea 0%,#b9aa92 40%,#3b5f8c 65%,#6f9a4a 100%)}
.steps-flag{left:0;top:43px;width:155px;height:136px}
.steps-flag-text{left:16px;top:82px;color:#fff;font-size:14.5px;line-height:2.05;font-weight:400}
.steps-flag-text b{font-weight:600}
.step-head{display:flex;align-items:flex-end}
.step-label{font-size:11px;line-height:1.05;color:#3a3a3a}
.step-title{font-size:14.5px;line-height:1.1;color:var(--title-blue)}
.step-head--dark .step-label{color:#fff}
.step-head--dark .step-title{color:var(--cyan)}
.body-col{font-size:6.6px;line-height:1.3;color:#444}
.body-col p{margin-bottom:5px;text-align:justify}
.body-col b{font-weight:700;color:#333}
.col-sub{color:var(--title-blue);font-size:7.4px;margin:3px 0 3px}
.plain-list{list-style:none;margin-bottom:6px}

/* inner spread – right */
.dark-panel{left:0;top:21px;width:405px;height:204px;background:var(--charcoal)}
.lower-area{left:0;top:225px;width:405px;height:299px;background:linear-gradient(180deg,#eceef0,#dfe2e5)}
.arrow-list{list-style:none;color:#fff;font-size:6.5px;line-height:1.2}
.arrow-list li{position:relative;padding-left:12px;margin-bottom:6px;text-align:justify}
.arrow-list li::before{content:"›";position:absolute;left:0;top:-1px;width:7px;height:7px;border:1px solid var(--cyan);border-radius:50%;color:var(--cyan);font-size:7px;line-height:6px;text-align:center}
.info-box{top:257px;width:178px;height:269px;background:linear-gradient(180deg,#ffffff 0%,#f4f5f7 60%,#e1e4e8 100%);box-shadow:0 2px 4px rgba(0,0,0,.12)}
.info-box-head{height:34px;background:linear-gradient(90deg,var(--cyan),#1b7fc6);color:#fff;text-align:center;font-size:11.6px;line-height:1.3;display:flex;align-items:center;justify-content:center;padding:0 4px}
.info-box-body{padding:9px 10px 0;font-size:6.6px;line-height:1.25}
.strategy{margin-bottom:8px}
.strategy h4{font-weight:400;color:var(--title-blue);font-size:6.9px;margin-bottom:2px}
.strategy p{padding-left:9px;color:#444;text-align:justify}
.profit{margin-bottom:9px;color:#444;text-align:justify}
</style>
</head>
<body>

<!-- Outer spread: back cover + front cover -->
<section class="spread spread--outer">
  <div class="page page--left">
    <div class="photo townhouse-photo" role="img" aria-label="Photograph of a row of multi-storey brick and siding townhouses under a blue sky"></div>
    <div class="abs profile-panel"></div>
    <div class="abs headshot" role="img" aria-label="Black and white portrait of the investor"></div>
    <h2 class="abs profile-name">Marisol Thornbury</h2>
    <p class="abs profile-bio">Marisol Thornbury is a residential real estate investor and physician with a passion for identifying and fixing problems through innovative and creative solutions. Her transition into commercial real estate is merely an extension of that passion. It is her professional experience in a demanding and competitive field, along with her tenacity and discipline for doing things effectively and efficiently, which instills confidence in her success as a CRE investor.</p>
    <div class="abs plan-sketch" role="img" aria-label="Faint architectural floor plan sketch"></div>
    <ul class="abs contact-list">
      <li><span class="ico"><svg width="8" height="6" viewBox="0 0 8 6"><rect x=".5" y=".5" width="7" height="5" fill="none" stroke="#fff" stroke-width=".9"/><path d="M.5 .5 4 3.4 7.5 .5" fill="none" stroke="#fff" stroke-width=".9"/></svg></span>info@marisolthornbury.com</li>
      <li><span class="ico"><svg width="8" height="8" viewBox="0 0 8 8"><circle cx="4" cy="4" r="3.3" fill="none" stroke="#fff" stroke-width=".9"/><path d="M.7 4h6.6M4 .7c-2 2-2 4.6 0 6.6M4 .7c2 2 2 4.6 0 6.6" fill="none" stroke="#fff" stroke-width=".7"/></svg></span>www.marisolthornbury.com</li>
      <li><span class="ico"></span>marisolthornbury.com</li>
      <li><span class="ico"><svg width="7" height="8" viewBox="0 0 7 8"><path d="M3.5 7.6S.6 4.6.6 3A2.9 2.9 0 0 1 6.4 3c0 1.6-2.9 4.6-2.9 4.6z" fill="#fff"/><circle cx="3.5" cy="3" r="1" fill="#9aa0a6"/></svg></span>marisolthornbury.com</li>
    </ul>
    <div class="footer-bar"></div>
  </div>

  <div class="page page--right">
    <h1 class="abs cover-title">MULTIFAMILY CASHFLOW INVESTMENT STRATEGY</h1>
    <div class="abs cover-band"></div>
    <div class="photo house-photo" role="img" aria-label="Photograph of a modern two-storey brick and stone house with garages and a green lawn at dusk"></div>
    <div class="abs cover-accent"></div>
    <p class="abs cover-tagline">Turning Underperforming Multifamily<br>Properties into Highly Profitable,<br>Cash-Flowing Assets.</p>
    <div class="footer-bar"></div>
  </div>
</section>

<!-- Inner spread: three steps -->
<section class="spread spread--inner">
  <div class="page page--left">
    <div class="photo couple-photo" role="img" aria-label="Photograph of a couple seen from behind, embracing while looking at a house"></div>
    <svg class="abs steps-flag" viewBox="0 0 155 136" aria-hidden="true">
      <defs><linearGradient id="flagGrad" x1="0" y1="0" x2="1" y2="1"><stop offset="0" stop-color="#22a6e3"/><stop offset="1" stop-color="#0b5c9e"/></linearGradient></defs>
      <polygon points="0,0 122,0 155,68 122,136 0,136" fill="url(#flagGrad)"/>
    </svg>
    <div class="abs steps-flag-text"><b>3 STEPS</b><br>FOR SUCCESS</div>

    <div class="abs step-head" style="left:18px;top:236px">
      <svg width="36" height="30" viewBox="0 0 36 30" aria-hidden="true" style="margin-right:8px">
        <path d="M3 14 12 6l9 8v9H3z" fill="none" stroke="#3a3a3a" stroke-width="2"/>
        <circle cx="18" cy="15" r="7" fill="#fff" stroke="#3a3a3a" stroke-width="2.4"/>
        <path d="M23 20l9 8" stroke="#3a3a3a" stroke-width="3.4" stroke-linecap="round"/>
      </svg>
      <div><div class="step-label">STEP 1</div><div class="step-title">BUY RIGHT</div></div>
    </div>

    <div class="abs body-col" style="left:14px;top:276px;width:184px">
      <div class="col-sub" style="margin-top:0">Value Add - Key questions when considering a property:</div>
      <ul class="plain-list">
        <li>• Who owns it?</li>
        <li>• How long have they owned it?</li>
        <li>• Why are they selling it?</li>
      </ul>
      <div class="col-sub">What to look for:</div>
      <p><b>Poor management</b> - typically by individual owners, families, or out of state management.</p>
      <p><b>Under market rents</b> - rates significantly below comparable prices in the area.</p>
      <p><b>Deferred maintenance</b> - this can be a sign of a motivated or “burned-out” seller. Light exterior and interior upgrades, e.g., paint, landscaping, carpet replacement, fixture and appliance upgrades, will have a significant impact.</p>
      <p><b>High vacancy</b> - often due to poor marketing.</p>
      <p><b>Motivated sellers</b> - allows for negotiation a lower price. Common motivators include divorce, bankruptcy, retirement, inherited properties, new investment opportunity, burnout, etc.</p>
      <p><b>Owner paid utilities</b> - allows for significant upside in income through implementing Ratio Utility Business System (RUBS).</p>
    </div>

    <div class="abs body-col" style="left:210px;top:258px;width:186px">
      <p>By tackling these issues, we will successfully reposition the property, which will significantly increase the income. As a result, the value of the property will also increase.</p>
      <p><b>Property Class</b> - B and C class properties in A and B neighborhoods - Prefer 1980’s or newer.</p>
      <p>These properties tend to house blue collar workers; don’t compete with new(er) construction; and don’t share the same challenges as C and D properties in C and D neighborhoods, which can encounter issues with crime, major disrepair, and increased vulnerability to economic downturns.</p>
      <p><b>Market Analysis</b> - Target emerging markets with population and job growth; low to median cost of housing which allows rent growth (e.g., Columbus, Oklahoma, Atlanta, Dallas, Phoenix); median income of ~$35k/yr; and landlord and business friendly rules and regulations (e.g., Ohio, Texas, Florida, Oklahoma, Colorado).</p>
      <p><b>Scale</b> - 60+ units to support effective, third-party professional management. Additionally, targeting 60+ units will increase the likelihood of stability by creating a buffer against tenant turnover and other unplanned expenses.</p>
      <p><b>Cash flow</b> - The property must generate cash flow from day one, before value add strategies are deployed.</p>
      <p>Buy on actual numbers instead of on pro forma analysis, which project or estimate financial return</p>
    </div>
  </div>

  <div class="page page--right">
    <div class="abs dark-panel"></div>
    <div class="abs lower-area"></div>

    <div class="abs step-head step-head--dark" style="left:18px;top:32px">
      <svg width="30" height="28" viewBox="0 0 30 28" aria-hidden="true" style="margin-right:5px">
        <rect x="2" y="18" width="4" height="9" fill="#22a6e3"/>
        <rect x="9" y="13" width="4" height="14" fill="#22a6e3"/>
        <rect x="16" y="9" width="4" height="18" fill="#22a6e3"/>
        <rect x="23" y="5" width="4" height="22" fill="#22a6e3"/>
        <path d="M1 15 10 7l6 4 11-10" fill="none" stroke="#22a6e3" stroke-width="2"/>
        <path d="M22 1h6v6" fill="none" stroke="#22a6e3" stroke-width="2"/>
      </svg>
      <div><div class="step-label">STEP 2</div><div class="step-title">FINANCE RIGHT</div></div>
    </div>
    <ul class="abs arrow-list" style="left:21px;top:74px;width:177px">
      <li>Longterm debt - with long terms and amortization periods.</li>
      <li>Non-recourse if possible. e.g., Fairhaven Mortgage, Fremont Housing Credit, CMBS. There is an extremely low foreclosure rate for these underwritten properties (1%-2%).</li>
      <li>No prepayment penalty.</li>
      <li>No due on sale clause.</li>
    </ul>

    <div class="abs step-head step-head--dark" style="left:211px;top:32px">
      <svg width="30" height="28" viewBox="0 0 30 28" aria-hidden="true" style="margin-right:8px">
        <path d="M2 13 15 2l13 11" fill="none" stroke="#22a6e3" stroke-width="2.6"/>
        <path d="M6 12v14h18V12" fill="none" stroke="#22a6e3" stroke-width="2.4"/>
        <circle cx="15" cy="18" r="4" fill="none" stroke="#22a6e3" stroke-width="2"/>
        <circle cx="15" cy="18" r="1.3" fill="#22a6e3"/>
      </svg>
      <div><div class="step-label">STEP 3</div><div class="step-title">MANAGE RIGHT</div></div>
    </div>
    <ul class="abs arrow-list" style="left:214px;top:74px;width:182px">
      <li>Third-Party Management with experience in this specific class of multifamily real estate.<br>• Sizable but not too large that our property gets lost.<br>• Only in property management, not acquisition or development so that there is no conflict of interest.</li>
      <li>Use of Sole Purpose Entity Structures, e.g., LLC’s for asset protection.</li>
      <li>Optimization through use of systems.</li>
      <li>Tenant satisfaction - Ensure great customer service to the tenant, e.g., 24 hour response to maintenance requests, cleanliness, and security. Happy tenants who feel heard and cared for, don’t leave, which limits tenant turnover, and lowers expenses.</li>
      <li>Increase the “curb appeal” - Freshened exterior with modern paint schemes, landscaping, and new signage. Rebranding with a name change, webpage, etc.</li>
    </ul>

    <div class="abs info-box" style="left:18px">
      <div class="info-box-head">5 STRATEGIES FOR INCREASING INCOME</div>
      <div class="info-box-body">
        <div class="strategy"><h4>1. Fill vacant units at market rate</h4><p>After light renovation (&lt; $1,000 per unit) modern, two-tone paint schemes (white trim, taupe/light grey walls); vinyl wood plank flooring to replace carpet; cleaning of existing carpet.</p></div>
        <div class="strategy"><h4>2. Employ RUBS, where applicable</h4><p>Pre-calculated formula for billing back a tenant’s utilities. Water, sewer, trash, gas/electric.</p></div>
        <div class="strategy"><h4>3. Gradually raise existing tenants<br>&nbsp;&nbsp;&nbsp;to market rate AFTER adding value</h4><p>Improve the exterior “curb appeal” - power washing, landscaping, painting. Inexpensive and effective.</p></div>
        <div class="strategy"><h4>4. Fees - Pet fees; deposits; late fees<br>&nbsp;&nbsp;&nbsp;(without exception); move-in fees</h4></div>
        <div class="strategy"><h4>5. Lower expenses through renegotiation of<br>&nbsp;&nbsp;&nbsp;contracts</h4></div>
      </div>
    </div>

    <div class="abs info-box" style="left:211px">
      <div class="info-box-head">5 WAYS TO PROFIT</div>
      <div class="info-box-body" style="padding-top:11px">
        <p class="profit">1. Monthly Cash Flow - from day one. Conservative estimation of 9% or higher cash on cash return.</p>
        <p class="profit">2. Equity through principle pay down - As the tenants pay down the mortgage, your equity continues to increase and creates true wealth.</p>
        <p class="profit">3. Reduced or even elimination of taxes through depreciation by doing cost segregation.</p>
        <p class="profit">4. Cash out refinancing - into non-recourse debt (if not already); return of original capital plus additional monies that can be used towards reinvestment into the asset and future assets.</p>
        <p class="profit">5. Forced Appreciation - by repositioning the asset through the methods previously discussed. Potential to double the original investment at the time of sale, which could occur in 5-7 years or sooner depending on the market.</p>
      </div>
    </div>
  </div>
</section>

</body>
</html>
```